Q&L Summit Holdings Business Cards

Design Business cards in a format where I can change the information and utilize a third party buisness card printing company

Contact Information for Business Card

Want Logo and Name on Back. Looking for Spot UV style shine on Logo. Probably Black background. Want smaller logo on front with contact details. Like rounded edges or something else interesting.

Requirements
Must have
• Strong masculine look.

```html
<!DOCTYPE html>
<html lang="en">
<head>
<meta charset="UTF-8">
<title>Q&amp;L Summit Holdings — Business Cards</title>
<link href="https://fonts.googleapis.com/css2?family=Oswald:wght@500&family=Jost:wght@400;500&display=swap" rel="stylesheet">
<style>
  :root {
    --page-bg: #2a2a2a;
    --card-black: #1c1c1c;
    --card-edge: #262626;
    --ink-white: #f2f2f2;
    --ink-soft: #d9d9d9;
    --uv-gloss: #3e3e3e;
    --uv-gloss-back: #464646;
  }
  * { margin: 0; padding: 0; box-sizing: border-box; }
  html, body {
    width: 1200px;
    height: 900px;
    overflow: hidden;
    background: var(--page-bg);
  }
  .canvas {
    position: relative;
    width: 1200px;
    height: 900px;
    display: flex;
    flex-direction: column;
    align-items: center;
    justify-content: center;
    gap: 34px;
  }
  .card {
    position: relative;
    width: 600px;
    height: 343px;
    background: var(--card-black);
    border: 1px solid var(--card-edge);
    border-radius: 10px;
    box-shadow: 0 14px 30px rgba(0,0,0,0.45);
  }

  /* Back of card */
  .card-back {
    display: flex;
    align-items: center;
    justify-content: center;
  }
  .back-brand {
    font-family: "Jost", sans-serif;
    font-weight: 500;
    font-size: 34px;
    letter-spacing: 4px;
    text-transform: uppercase;
    color: var(--uv-gloss-back);
  }

  /* Front of card */
  .front-brand {
    position: absolute;
    top: 38px;
    right: 36px;
    font-family: "Jost", sans-serif;
    font-weight: 500;
    font-size: 15px;
    letter-spacing: 2px;
    text-transform: uppercase;
    color: var(--uv-gloss);
    text-align: right;
  }
  .identity {
    position: absolute;
    top: 118px;
    left: 130px;
    width: 170px;
    text-align: right;
  }
  .person-name {
    font-family: "Oswald", sans-serif;
    font-weight: 500;
    font-size: 33px;
    line-height: 1;
    letter-spacing: 0.5px;
    color: var(--ink-white);
    text-transform: uppercase;
    white-space: nowrap;
  }
  .person-role {
    margin-top: 6px;
    font-family: "Jost", sans-serif;
    font-size: 16px;
    color: var(--ink-soft);
  }
  .divider {
    position: absolute;
    top: 120px;
    left: 318px;
    width: 1.5px;
    height: 64px;
    background: var(--ink-soft);
  }
  .contact-list {
    position: absolute;
    top: 122px;
    left: 334px;
    list-style: none;
    font-family: "Jost", sans-serif;
    font-size: 14.5px;
    letter-spacing: 0.6px;
    color: var(--ink-soft);
  }
  .contact-list li {
    display: flex;
    align-items: center;
    gap: 12px;
    height: 21px;
  }
  .contact-list svg {
    width: 14px;
    height: 14px;
    flex: none;
  }
  .address {
    position: absolute;
    left: 150px;
    bottom: 50px;
    font-family: "Jost", sans-serif;
    font-size: 16px;
    letter-spacing: 0.6px;
    color: var(--ink-soft);
  }
</style>
</head>
<body>
  <main class="canvas">
    <section class="card card-back" aria-label="Card back">
      <p class="back-brand">Q&amp;L Summit Holdings</p>
    </section>

    <section class="card card-front" aria-label="Card front">
      <p class="front-brand">Q&amp;L Summit Holdings</p>

      <div class="identity">
        <h1 class="person-name">Daniel Reyes</h1>
        <p class="person-role">CEO &amp; Founder</p>
      </div>

      <div class="divider"></div>

      <ul class="contact-list">
        <li>
          <svg viewBox="0 0 14 14" aria-hidden="true"><rect x="3.5" y="1" width="7" height="12" rx="1.2" fill="none" stroke="#8a8a8a" stroke-width="1.3"/><line x1="6" y1="11" x2="8" y2="11" stroke="#8a8a8a" stroke-width="1.2"/></svg>
          <span>000 111 2223</span>
        </li>
        <li>
          <svg viewBox="0 0 14 14" aria-hidden="true"><rect x="1" y="3" width="12" height="8.5" rx="1" fill="#8a8a8a"/><polyline points="1.5,3.5 7,8 12.5,3.5" fill="none" stroke="#1c1c1c" stroke-width="1.2"/></svg>
          <span>urname@email.com</span>
        </li>
        <li>
          <svg viewBox="0 0 14 14" aria-hidden="true"><circle cx="8" cy="6" r="4" fill="none" stroke="#8a8a8a" stroke-width="1.4"/><line x1="5" y1="9" x2="1.5" y2="12.5" stroke="#8a8a8a" stroke-width="1.6"/></svg>
          <span>www.yoursitename.com</span>
        </li>
      </ul>

      <p class="address">Your Street Address Here, NewYork city,1234</p>
    </section>
  </main>
</body>
</html>
```